Tarvik Plans - Worpress Design

We are a consultancy to help builders to optimize their planning in order to save building costs. For that reason we need a website to offer our services, present our history, the mission and offer a plug-in for a first contact (including calendar), testimonials, a blog etc.
As an idea, I really like: https://www.fendrowadvisory.de/
Later on the website should be programmed in www.quelvo.de in our Wordpress area. The text, of course, will be done by myself. The colors should be suitable to our recently designed logo.

```html
<!DOCTYPE html>
<html lang="en">
<head>
<meta charset="utf-8">
<title>Tarvik Plans – Consultancy for Builders</title>
<link rel="stylesheet" href="https://fonts.googleapis.com/css2?family=Michroma&family=Poppins:wght@300;400;500;600&display=swap">
<style>
:root{
  --gold:#c8923a;
  --gold-light:#e6bb62;
  --gold-dark:#9c6a22;
  --ink:#1b1b22;
  --night:#16161c;
  --text:#55565e;
  --muted:#8a8b93;
  --pale:#f1f2f4;
  --white:#ffffff;
  --line:#e4e4e8;
}
*{box-sizing:border-box;margin:0;padding:0}
html,body{width:1200px;height:5284px;overflow:hidden}
body{font-family:'Poppins',sans-serif;color:var(--text);background:var(--white);position:relative}
section,header,footer{position:absolute;left:0;width:1200px}
.abs{position:absolute}
.display{font-family:'Michroma',sans-serif;color:var(--ink);text-transform:uppercase;letter-spacing:3px;line-height:1.3}
.kicker{font-size:15px;color:var(--ink);font-weight:500}
.copy{font-size:14px;line-height:1.75;color:var(--text)}
.btn{position:absolute;display:inline-flex;align-items:center;justify-content:center;height:42px;padding:0 26px;border:1.5px solid var(--gold);border-radius:22px;font-size:12px;font-weight:500;color:var(--ink);background:var(--white);letter-spacing:.5px}
.btn.dark{background:transparent;color:var(--white)}
.photo{position:absolute;overflow:hidden}

/* header */
.site-header{top:0;height:120px;background:var(--white)}
.brand{position:absolute;display:flex;align-items:center;gap:10px;font-family:'Poppins',sans-serif;font-weight:600;font-size:20px;color:var(--gold);letter-spacing:1px}
.brand-mark{width:28px;height:28px;background:var(--gold)}
.topline{right:64px;top:14px;font-size:12px;color:var(--ink)}
.nav{right:64px;top:62px;display:flex;gap:42px;font-size:14px;color:var(--ink)}
.nav .active{color:var(--gold);border-bottom:2px solid var(--gold);padding-bottom:6px}

/* hero */
.hero{top:120px;height:620px;background:var(--pale);overflow:hidden}

/* services */
.services{top:740px;height:740px}
.service-card{position:absolute;top:272px;height:388px;border-radius:10px;overflow:hidden}
.service-card .caption{position:absolute;left:16px;bottom:18px;font-size:14px;color:var(--white);display:flex;align-items:center;gap:8px}
.service-card .caption i{width:22px;height:22px;border:1.5px solid var(--white);border-radius:4px;display:block}
.service-info{position:absolute;left:572px;top:460px;width:290px;height:180px;background:var(--white);border-radius:10px;padding:20px;box-shadow:0 6px 20px rgba(0,0,0,.12)}
.service-info .icon{width:38px;height:38px;border-radius:6px;background:var(--gold-light);margin-bottom:12px}
.service-info h4{font-size:16px;color:var(--ink);font-weight:500;margin-bottom:6px}
.service-info p{font-size:12px;line-height:1.6}
.slider-arrow{position:absolute;left:1152px;top:598px;width:30px;height:30px;background:var(--gold);border-radius:4px}

/* about */
.about{top:1480px;height:652px}
.badge{position:absolute;left:150px;top:400px;width:210px;height:100px;background:linear-gradient(90deg,var(--gold-dark),var(--gold-light));clip-path:polygon(0 0,82% 0,100% 50%,82% 100%,0 100%);color:var(--white);padding:18px 22px}
.badge b{font-size:24px;font-weight:600;display:block}
.badge span{font-size:12px}

/* history */
.history{top:2132px;height:740px;background:var(--night)}
.history-bg{position:absolute;inset:0 0 340px 0;background:linear-gradient(135deg,#2a2a33,#17171d 60%,#25252d)}
.video{left:64px;top:348px;width:1072px;height:360px;border-radius:12px;overflow:hidden}

/* blog */
.blog{top:2872px;height:680px}
.post{position:absolute;top:136px;width:348px;height:444px;border:1px solid var(--line);border-radius:10px;overflow:hidden;background:var(--white)}
.post .thumb{height:222px}
.post h3{font-size:17px;font-weight:600;color:var(--ink);line-height:1.4;margin:28px 16px 10px}
.post p{font-size:12px;line-height:1.6;margin:0 16px}
.post .btn{left:16px;bottom:20px;height:38px}

/* testimonials */
.testimonials{top:3552px;height:470px;background:linear-gradient(100deg,var(--gold-dark),var(--gold-light) 55%,var(--gold))}
.quote{position:absolute;top:140px;width:516px;height:190px;background:var(--white);border-radius:0 22px 22px 22px;padding:30px 30px 0 94px}
.quote .mark{position:absolute;left:26px;top:60px;font-family:Georgia,serif;font-size:90px;line-height:1;color:var(--gold)}
.quote p{font-size:14px;line-height:1.7}
.person{position:absolute;top:368px;display:flex;align-items:center;gap:14px;color:var(--white)}
.person i{width:62px;height:62px;border-radius:50%;background:linear-gradient(135deg,#e9d6c2,#9a7a62);border:3px solid var(--white);display:block}
.person b{font-weight:500;font-size:15px;display:block;color:var(--ink)}
.person span{font-size:11px;color:var(--ink)}
.dots{position:absolute;left:0;width:1200px;top:446px;display:flex;justify-content:center;gap:8px}
.dots i{width:8px;height:8px;border-radius:50%;background:rgba(255,255,255,.55);display:block}
.dots i.on{background:var(--white);width:20px;border-radius:4px}

/* contact */
.contact{top:4022px;height:498px}
.contact-box{position:absolute;left:64px;top:308px;width:1072px;height:310px;background:var(--white);border-radius:10px;box-shadow:0 10px 30px rgba(0,0,0,.18);overflow:hidden;z-index:2}
.field{position:absolute;height:40px;border:1px solid var(--line);border-radius:4px;font-size:12px;color:var(--muted);padding:11px 14px}

/* footer */
.site-footer{top:4520px;height:764px;background:var(--night);color:#c9c9d0}
.foot-col{position:absolute;top:340px}
.foot-col h5{font-size:13px;font-weight:500;color:var(--gold);letter-spacing:1px;margin-bottom:18px;text-transform:uppercase}
.foot-col li{list-style:none;font-size:12px;margin-bottom:12px}
.social{position:absolute;left:64px;top:450px;display:flex;gap:12px}
.social i{width:30px;height:30px;border-radius:50%;background:var(--gold);display:block}
.copyright{position:absolute;left:0;width:1200px;top:704px;text-align:center;font-size:11px;letter-spacing:1px;border-top:1px solid #2b2b33;padding-top:22px}
</style>
</head>
<body>

<header class="site-header">
  <div class="brand" style="left:64px;top:42px"><span class="brand-mark"></span>TARVIK PLANS</div>
  <div class="abs topline">Call Us: +1 (555) 010 4821</div>
  <nav class="abs nav">
    <span class="active">Home</span><span>About Us</span><span>Services</span><span>Testimonials</span><span>Blog</span><span>Contact Us</span>
  </nav>
</header>

<section class="hero">
  <svg class="abs" style="left:0;top:0" width="1200" height="620" viewBox="0 0 1200 620">
    <defs>
      <linearGradient id="heroGold" x1="0" y1="0" x2="1" y2="1">
        <stop offset="0" stop-color="#e6bb62"/><stop offset=".5" stop-color="#b8842f"/><stop offset="1" stop-color="#8f5f1c"/>
      </linearGradient>
      <linearGradient id="heroPhoto" x1="0" y1="0" x2="1" y2="1">
        <stop offset="0" stop-color="#cfd3d8"/><stop offset=".5" stop-color="#8b8f97"/><stop offset="1" stop-color="#3d4048"/>
      </linearGradient>
    </defs>
    <polygon points="440,620 560,500 560,620" fill="#e2e4e8"/>
    <polygon points="560,620 810,0 950,0 700,620" fill="url(#heroGold)"/>
    <polygon points="700,620 950,0 1200,0 1200,620" fill="url(#heroPhoto)" role="img" aria-label="Photo of business team meeting around a laptop in a bright office"/>
  </svg>
  <div class="abs kicker" style="left:64px;top:160px;font-size:20px">Builders to</div>
  <h1 class="abs display" style="left:64px;top:196px;font-size:38px;line-height:1.45;width:520px">Optimize their planning</h1>
  <p class="abs copy" style="left:64px;top:330px;width:380px;font-size:13px">Duis aute irure dolor in reprehenderit in voluptate velit esse cillum.</p>
  <span class="btn" style="left:64px;top:418px">EXPLORE MORE</span>
</section>

<section class="services">
  <div class="abs kicker" style="left:64px;top:104px">Our Services</div>
  <h2 class="abs display" style="left:64px;top:136px;font-size:30px;width:560px;line-height:1.5">We offer a wide varity services</h2>
  <div class="service-card" style="left:-20px;width:260px;background:linear-gradient(160deg,#b6a895,#5e564c)" role="img" aria-label="Photo of consultants reviewing documents"><div class="caption"><i></i>Quis Ponsequntur</div></div>
  <div class="service-card" style="left:256px;width:280px;background:linear-gradient(160deg,#d4cbc2,#7c6e64)" role="img" aria-label="Photo of a smiling businesswoman in a meeting"><div class="caption"><i></i>Quis Ponsequntur</div></div>
  <div class="service-card" style="left:560px;width:352px;background:linear-gradient(160deg,#c7d0d9,#55606c)" role="img" aria-label="Photo of modern glass office towers"></div>
  <div class="service-card" style="left:852px;width:280px;background:linear-gradient(160deg,#a9a6a4,#2f2e33)" role="img" aria-label="Photo of business partners shaking hands"><div class="caption"><i></i>Quis Ponsequntur</div></div>
  <div class="service-info"><div class="icon"></div><h4>Finibus Bonorum</h4><p>Sed ut perspiciatis unde omnis iste natus error sit voluptatem accusantium doloremque.</p></div>
  <div class="slider-arrow"></div>
</section>

<section class="about">
  <svg class="abs" style="left:60px;top:40px" width="420" height="520" viewBox="0 0 420 520">
    <defs>
      <linearGradient id="aboutA" x1="0" y1="0" x2="1" y2="1"><stop offset="0" stop-color="#cdc3b8"/><stop offset="1" stop-color="#6d5f54"/></linearGradient>
      <linearGradient id="aboutB" x1="0" y1="0" x2="1" y2="1"><stop offset="0" stop-color="#e0d8ce"/><stop offset="1" stop-color="#8a7c70"/></linearGradient>
    </defs>
    <polygon points="200,0 330,130 200,260 70,130" fill="url(#aboutA)" role="img" aria-label="Photo of a woman at a laptop"/>
    <polygon points="340,140 420,220 340,300 260,220" fill="url(#aboutB)" role="img" aria-label="Photo of an office detail"/>
    <polygon points="200,270 340,410 200,520 80,410" fill="url(#aboutB)" role="img" aria-label="Photo of two colleagues working together"/>
    <polygon points="60,150 180,270 60,390 0,270" fill="url(#aboutA)" role="img" aria-label="Photo of a team discussion"/>
  </svg>
  <div class="badge"><b>1.5 K</b><span>Satisfied Clients</span></div>
  <div class="abs kicker" style="left:668px;top:92px">About Us</div>
  <h2 class="abs display" style="left:668px;top:124px;font-size:30px;width:470px;line-height:1.5">We are a consultancy to help builders</h2>
  <p class="abs copy" style="left:668px;top:282px;width:460px">Sed ut perspiciatis unde omnis iste natus error sit voluptatem accusantium doloremque laudantium, totam rem aperiam, eaque ipsa quae ab illo inventore veritatis et quasi architecto beatae vitae dicta sunt explicabo. Nemo enim ipsam voluptatem quia voluptas sit aspernatur aut odit aut fugit.</p>
  <span class="btn" style="left:668px;top:448px">READ MORE</span>
</section>

<section class="history">
  <div class="history-bg" role="img" aria-label="Dark photo of an office building facade"></div>
  <h2 class="abs display" style="left:0;width:1200px;top:44px;text-align:center;color:var(--white);font-size:30px">Our History</h2>
  <p class="abs copy" style="left:84px;width:1032px;top:104px;text-align:center;color:#d4d4da">Sed ut perspiciatis unde omnis iste natus error sit voluptatem accusantium doloremque laudantium, totam rem aperiam, eaque ipsa quae ab illo inventore veritatis et quasi architecto beatae vitae dicta sunt explicabo. Nemo enim ipsam voluptatem quia voluptas sit aspernatur aut odit aut fugit, sed quia consequuntur magni dolores eos qui ratione voluptatem sequi nesciunt.</p>
  <span class="btn dark" style="left:538px;top:252px">READ MORE</span>
  <div class="photo video" role="img" aria-label="Video still of a team at work in a dim office" style="background:linear-gradient(120deg,#2c2c33,#4a4a52 50%,#2a2a30)">
    <svg class="abs" style="left:0;top:0" width="1072" height="360" viewBox="0 0 1072 360">
      <polygon points="660,360 760,230 1072,230 1072,360" fill="#3a3a42"/>
      <circle cx="64" cy="180" r="30" fill="rgba(255,255,255,.18)"/>
      <polygon points="56,166 78,180 56,194" fill="#ffffff"/>
    </svg>
    <span class="btn dark" style="left:720px;top:252px">READ MORE</span>
  </div>
</section>

<section class="blog">
  <h2 class="abs display" style="left:0;width:1200px;top:64px;text-align:center;font-size:30px">Recent Blog</h2>
  <article class="post" style="left:64px">
    <div class="thumb" style="background:linear-gradient(150deg,#d8d2c8,#7e7468)" role="img" aria-label="Photo of colleagues gathered at a desk"></div>
    <h3>Excepteur sint occaecat cupidatat non proident</h3>
    <p>Sed ut perspiciatis unde omnis iste natus error sit voluptatem accusantium doloremque laudantium.</p>
    <span class="btn">READ MORE</span>
  </article>
  <article class="post" style="left:426px">
    <div class="thumb" style="background:linear-gradient(150deg,#e4ddd2,#8c7f70)" role="img" aria-label="Photo of a meeting with plans on the table"></div>
    <h3>Excepteur sint occaecat cupidatat non proident</h3>
    <p>Sed ut perspiciatis unde omnis iste natus error sit voluptatem accusantium doloremque laudantium.</p>
    <span class="btn">READ MORE</span>
  </article>
  <article class="post" style="left:788px">
    <div class="thumb" style="background:linear-gradient(150deg,#efeae3,#9d9084)" role="img" aria-label="Photo of a team reviewing a laptop"></div>
    <h3>Excepteur sint occaecat cupidatat non proident</h3>
    <p>Sed ut perspiciatis unde omnis iste natus error sit voluptatem accusantium doloremque laudantium.</p>
    <span class="btn">READ MORE</span>
  </article>
</section>

<section class="testimonials">
  <h2 class="abs display" style="left:0;width:1200px;top:64px;text-align:center;color:var(--white);font-size:30px">Testimonials</h2>
  <div class="quote" style="left:64px"><span class="mark">&ldquo;</span><p>Sed ut perspiciatis unde omnis iste natus error sit voluptatem accusantium doloremque laudantium, totam rem aperiam, eaque ipsa quae ab illo inventore veritatis et quasi architecto beatae vitae dicta sunt explicabo.</p></div>
  <div class="person" style="left:70px"><i role="img" aria-label="Client portrait"></i><div><b>Mara Lind</b><span>Digital Marketing Executive</span></div></div>
  <div class="quote" style="left:620px"><span class="mark">&ldquo;</span><p>Sed ut perspiciatis unde omnis iste natus error sit voluptatem accusantium doloremque laudantium, totam rem aperiam, eaque ipsa quae ab illo inventore veritatis et quasi architecto beatae vitae dicta sunt explicabo.</p></div>
  <div class="person" style="left:626px"><i role="img" aria-label="Client portrait"></i><div><b>Ines Holt</b><span>Senior Content Marketing</span></div></div>
  <div class="dots"><i class="on"></i><i></i><i></i></div>
</section>

<section class="contact">
  <div class="abs kicker" style="left:0;width:1200px;top:204px;text-align:center">Contact Us</div>
  <h2 class="abs display" style="left:0;width:1200px;top:236px;text-align:center;font-size:30px">We alway here to helps you</h2>
</section>

<div class="contact-box" style="top:4330px">
  <div class="photo" style="left:0;top:0;width:436px;height:310px;background:linear-gradient(140deg,#cfc9c0,#77706a 60%,#4f5a3e)" role="img" aria-label="Photo of consultants presenting an architectural building model"></div>
  <div class="field" style="left:480px;top:68px;width:262px">Name</div>
  <div class="field" style="left:760px;top:68px;width:262px">Email</div>
  <div class="field" style="left:480px;top:122px;width:262px">Phone</div>
  <div class="field" style="left:760px;top:122px;width:262px">Schedule</div>
  <div class="field" style="left:480px;top:176px;width:542px;height:70px">Message</div>
  <span class="btn" style="left:480px;top:258px;height:36px;font-size:11px">SEND MESSAGE</span>
</div>

<footer class="site-footer">
  <div class="brand" style="left:64px;top:336px;font-size:18px"><span class="brand-mark" style="width:24px;height:24px"></span>TARVIK PLANS</div>
  <p class="abs" style="left:64px;top:384px;width:330px;font-size:12px;line-height:1.7">Sed ut perspiciatis unde omnis iste natus error sit voluptatem accusantium doloremque laudantium, totam rem aperiam.</p>
  <div class="social"><i></i><i></i><i></i></div>
  <div class="foot-col" style="left:472px"><h5>Quick Links</h5><ul><li>Home</li><li>About Us</li><li>Services</li><li>Testimonials</li><li>Blog</li><li>Contact Us</li></ul></div>
  <div class="foot-col" style="left:688px"><h5>Services</h5><ul><li>Finibus Bonorum</li><li>Neque Porrocurt</li><li>Architecto Beatae</li><li>Modi Tempora</li><li>Iure Reprehenderit</li></ul></div>
  <div class="foot-col" style="left:912px"><h5>Contacts</h5><ul><li>766 Lorem ipsum dolor sit amet,<br>Elmsford, T42 KX</li><li>+1 (555) 010 4821</li><li>hello@tarvikplans.com</li></ul></div>
  <div class="copyright">COPYRIGHT © 2023 TARVIK PLANS. ALL RIGHTS RESERVED.</div>
</footer>

</body>
</html>
```